Velmoran Tabletop Deck Company (southern african focus for now) needs a e-commerce website

We need a website design for a playing card company based in Southern Africa/United States. We make locally-sourced playing cards (standard 52 card deck, with customized fronts and backs) for everyone and collaborate with local artists to uplift their talents, while celebrating their nation's culture, heritage, beauty and identity. We would like to see designs that use the colours blue (see flag of Eswatini as starting product), white and some red accents (or your recommendation). The final design should communicate elegance, fun and sustainable prosperity.

Target Market(s)

Everyone loves playing cards. From the solo adventurer to the party host, first time learner or expert, young, middle and old, we need to attract a broad audience that appreciates the finer things and supports sustainable, environmentally contentiousness causes that support the local economy and uplift local talent - thing global, act local.

Number of Pages Required

4 page

Font styles to use
Serif
Sans Serif

Requirements
Must have
• Pages to include Home (Main), About (Our Story), Shop and Contact
Nice to have
• While designs may be static, elements of graceful movement would be desirable. Perhaps functionality of scrolling down on homepage showing playing cards in use, front and back. Quindle and Zorbix store's capture that elegant yet rich look.
Should not have
• Too many products. We focus on 1-2.

```html
<!DOCTYPE html>
<html lang="en">
<head>
<meta charset="utf-8">
<title>Velmoran — Playing Cards</title>
<link href="https://fonts.googleapis.com/css2?family=Playfair+Display:wght@400;700&family=Roboto:wght@400;500&display=swap" rel="stylesheet">
<style>
:root{
  --red:#b3191d;
  --deep-red:#7e0b10;
  --blue:#2b3f8e;
  --flag-blue:#3e5eb9;
  --flag-yellow:#ffd900;
  --deck-violet:#5b5a96;
  --deck-orange:#e0482a;
  --deck-gold:#f5c02a;
  --ink:#222;
  --muted:#444;
  --line:#cfcfcf;
  --soft:#efeeec;
  --white:#fff;
  --serif:'Playfair Display', Georgia, serif;
  --sans:'Roboto', Arial, sans-serif;
}
*{box-sizing:border-box;margin:0;padding:0}
html,body{width:1200px;height:3493px;overflow:hidden;background:var(--white);color:var(--ink)}
.page{position:relative;width:1200px;height:3493px;overflow:hidden}
.abs{position:absolute}
.btn{position:absolute;display:flex;align-items:center;justify-content:center;background:var(--red);color:var(--white);font-family:var(--serif);font-weight:700;font-size:15px;letter-spacing:.3px;border-radius:22px;height:43px;width:148px;text-transform:uppercase}

/* header */
.site-header{position:absolute;top:0;left:0;width:1200px;height:72px;background:var(--white);z-index:2}
.brand{position:absolute;left:172px;top:17px;display:flex;align-items:center;gap:8px;font-family:var(--serif);font-size:29px;color:var(--ink)}
.brand-dot{width:13px;height:13px;border-radius:50%;background:var(--ink)}
.nav{position:absolute;top:26px;font-family:var(--serif);font-size:16px;color:#333}
.nav.active{color:var(--red)}
.lang{position:absolute;left:801px;top:28px;display:flex;align-items:center;gap:6px;font-family:var(--serif);font-size:12px;color:#555}
.lang-flag{width:28px;height:17px;background:linear-gradient(var(--flag-blue) 0 22%,var(--flag-yellow) 22% 30%,var(--red) 30% 70%,var(--flag-yellow) 70% 78%,var(--flag-blue) 78%)}
.header-icons{position:absolute;left:934px;top:26px;display:flex;gap:16px}

/* hero */
.hero{position:absolute;top:72px;left:0;width:1200px;height:648px;
  background:
    radial-gradient(circle at 12% 18%,rgba(200,60,60,.35),transparent 22%),
    radial-gradient(circle at 85% 22%,rgba(190,50,50,.3),transparent 20%),
    radial-gradient(circle at 70% 70%,rgba(210,180,120,.25),transparent 24%),
    radial-gradient(circle at 20% 75%,rgba(230,230,230,.22),transparent 22%),
    radial-gradient(circle at 45% 40%,rgba(240,240,240,.18),transparent 26%),
    radial-gradient(ellipse at center,#6d6b6b 0%,#4e4c4c 55%,#2f2e2e 100%)}
.hero:after{content:"";position:absolute;inset:0;background:rgba(0,0,0,.18)}
.hero-inner{position:absolute;inset:0;z-index:1}
.hero-title{position:absolute;top:205px;width:100%;text-align:center;font-family:var(--serif);font-size:98px;color:var(--white);font-weight:400}
.dots{position:absolute;top:576px;left:527px;display:flex;gap:4px}
.dots span{width:34px;height:4px;background:var(--white)}

/* welcome */
.section-title{position:absolute;width:100%;text-align:center;font-family:var(--serif);font-weight:400;font-size:45px;color:var(--ink)}
.welcome-text{position:absolute;left:100px;width:1000px;top:852px;text-align:center;font-family:var(--sans);font-size:13.6px;line-height:23px;color:var(--muted)}
.welcome-text span,.products-text span{display:block;white-space:nowrap}

/* gallery */
.tile{position:absolute;top:1063px;height:320px;overflow:hidden}
.play{position:absolute;left:157px;top:130px;width:62px;height:62px;border-radius:50%;background:var(--red);display:flex;align-items:center;justify-content:center}

/* products */
.products-title{position:absolute;left:170px;top:1508px;font-family:var(--serif);font-size:45px;font-weight:400}
.products-text{position:absolute;left:173px;top:1573px;font-family:var(--sans);font-size:13.6px;line-height:23px;color:var(--muted)}
.deck-edge{position:absolute;border-radius:16px;background:var(--deck-violet)}

/* posts */
.posts{position:absolute;left:0;top:1946px;width:1200px;height:525px;background:var(--soft)}
.post{position:absolute;top:146px;width:266px}
.post-img{height:224px}
.post-title{margin-top:22px;text-align:center;font-family:var(--serif);font-size:23px;line-height:27px;color:#333}

/* faq */
.faq{position:absolute;left:328px;width:544px}
.faq-item{height:66px;border-bottom:1px solid var(--line);display:flex;align-items:center;gap:12px;font-family:var(--serif);font-size:21px;color:#333}
.plus{width:32px;height:30px;background:var(--red);position:relative;flex:none}
.plus:before,.plus:after{content:"";position:absolute;background:var(--white);left:50%;top:50%;transform:translate(-50%,-50%)}
.plus:before{width:14px;height:3px}
.plus:after{width:3px;height:14px}
.deco-card{position:absolute;background:linear-gradient(160deg,#ffffff,#f1f1f1);border-radius:12px;box-shadow:0 8px 26px rgba(0,0,0,.12)}

/* footer */
.site-footer{position:absolute;left:0;top:3135px;width:1200px;height:358px;
  background:radial-gradient(ellipse at 30% 30%,#34499a,transparent 60%),radial-gradient(ellipse at 80% 80%,#24377f,transparent 60%),var(--blue)}
.emblem{position:absolute;left:525px;top:3040px;width:150px;height:150px;border-radius:50%;background:var(--white)}
.emblem-mark{position:absolute;left:48px;top:12px;width:54px;height:120px;border-radius:27px;background:linear-gradient(90deg,var(--flag-blue) 0 22%,var(--flag-yellow) 22% 30%,var(--red) 30% 70%,var(--flag-yellow) 70% 78%,var(--flag-blue) 78%)}
.contact{position:absolute;top:3228px;display:flex;align-items:center;gap:10px;color:var(--white);font-family:var(--sans);font-size:17px;line-height:24px}
.footer-rule{position:absolute;left:235px;top:3320px;width:730px;height:1px;background:rgba(255,255,255,.35)}
.socials{position:absolute;left:522px;top:3349px;display:flex;gap:26px}
.socials span{width:20px;height:20px;border-radius:50%;background:var(--white)}
.copyright{position:absolute;top:3392px;width:100%;text-align:center;font-family:var(--serif);font-size:12.5px;color:var(--white)}
.payments{position:absolute;left:524px;top:3432px;display:flex;gap:9px}
.payments span{width:33px;height:19px;border-radius:3px;background:rgba(255,255,255,.85)}
</style>
</head>
<body>
<div class="page">

  <header class="site-header">
    <div class="brand"><span class="brand-dot"></span>Velmoran</div>
    <span class="nav active" style="left:461px">Home</span>
    <span class="nav" style="left:541px">About</span>
    <span class="nav" style="left:622px">Shop</span>
    <span class="nav" style="left:697px">Contact</span>
    <div class="lang"><span class="lang-flag"></span>Eswatini ▾</div>
    <div class="header-icons">
      <svg width="18" height="18" viewBox="0 0 18 18" fill="none" stroke="#222" stroke-width="1.6"><circle cx="9" cy="6" r="4"/><path d="M2 17c1-4 4-6 7-6s6 2 7 6"/></svg>
      <svg width="18" height="18" viewBox="0 0 18 18" fill="none" stroke="#222" stroke-width="1.8"><circle cx="7.5" cy="7.5" r="5.5"/><path d="M12 12l5 5"/></svg>
      <svg width="20" height="20" viewBox="0 0 20 20"><path d="M3 6h12v12H3z" fill="none" stroke="#222" stroke-width="1.8"/><path d="M6 6V4a3 3 0 0 1 6 0v2" fill="none" stroke="#222" stroke-width="1.6"/><circle cx="16" cy="4" r="4" fill="#b3191d"/></svg>
    </div>
  </header>

  <section class="hero" role="img" aria-label="Scattered playing cards photographed from above">
    <div class="hero-inner">
      <h1 class="hero-title">Velmoran</h1>
      <span class="btn" style="left:526px;top:331px">Read More</span>
      <div class="dots"><span></span><span></span><span></span><span></span></div>
    </div>
  </section>

  <h2 class="section-title" style="top:762px">Welcome to Velmoran</h2>
  <p class="welcome-text">
    <span>At vero eos et accusamus et iusto odio dignissimos ducimus qui blanditiis praesentium voluptatum deleniti atque corrupti quos do-</span>
    <span>lores et quas molestias excepturi sint occaecati cupiditate non provident, similique sunt in culpa qui officia deserunt mollitia animi,</span>
    <span>id est laborum et dolorum fuga. Et harum quidem rerum facilis est et expedita distinctio. Nam libero tempore, cum soluta nobis est</span>
    <span>eligendi optio cumque nihil impedit quo minus id quod maxime placeat facere possimus, omnis voluptas assumenda est,</span>
  </p>
  <span class="btn" style="left:526px;top:973px">Read More</span>

  <div class="tile" style="left:0;width:382px;background:linear-gradient(var(--flag-blue) 0 18%,var(--flag-yellow) 18% 24%,var(--red) 24% 76%,var(--flag-yellow) 76% 82%,var(--flag-blue) 82%)" role="img" aria-label="Flag of Eswatini with its central shield"></div>
  <div class="tile" style="left:405px;width:386px;background:linear-gradient(#2f3a22 0%,#4a5236 28%,#7a6a55 45%,#9a8a78 58%,#d8d8d4 68%,#a5a49e 82%,#8a8a86 100%)" role="img" aria-label="Video still of a waterfall over rocks">
    <span class="play"><svg width="18" height="18" viewBox="0 0 18 18"><path d="M4 1l12 8-12 8z" fill="#fff"/></svg></span>
  </div>
  <div class="tile" style="left:812px;width:388px;background:radial-gradient(ellipse at 50% 50%,#f3f1ee 0%,#e9e6e2 18%,transparent 30%),radial-gradient(ellipse at 75% 35%,#1c1c1c 0%,#2a2a2a 14%,transparent 22%),radial-gradient(ellipse at 55% 45%,#c21a20,var(--deep-red))" role="img" aria-label="Fan of four aces beside a dark card back on red"></div>

  <h2 class="products-title">Our Products</h2>
  <p class="products-text">
    <span>At vero eos et accusamus et iusto odio dignissimos ducimus</span>
    <span>qui blanditiis praesentium voluptatum deleniti atque corrupti</span>
    <span>quos dolores et quas molestias excepturi sint occaecati cupid</span>
    <span>itate non provident, similique sunt in culpa qui officia deserunt</span>
    <span>mollitia animi, id est laborum et dolorum fuga. Et harum quide</span>
    <span>rerum facilis est et expedita distinctio. Nam libero tempore,</span>
    <span>cum soluta nobis est eligendi optio cumque nihil impedit quo</span>
    <span>minus id quod maxime placeat facere possimus, omnis volu</span>
    <span>ptas assumenda est,</span>
  </p>
  <span class="btn" style="left:174px;top:1806px">View More</span>
  <div class="deck-edge" style="left:678px;top:1510px;width:262px;height:358px;background:#4b4a80"></div>
  <div class="deck-edge" style="left:682px;top:1504px;width:264px;height:360px;background:#6a69a3"></div>
  <div class="abs" style="left:686px;top:1496px;width:263px;height:362px;border-radius:16px;background:linear-gradient(90deg,var(--deck-violet) 0 10%,var(--deck-gold) 10% 16%,var(--deck-orange) 16% 84%,var(--deck-gold) 84% 90%,var(--deck-violet) 90%)" role="img" aria-label="Deck of cards with Eswatini flag card back"></div>

  <section class="posts">
    <h2 class="section-title" style="top:58px">Latest Posts</h2>
    <div class="post" style="left:191px"><div class="post-img" style="background:linear-gradient(90deg,#6b5a4a 0 3%,var(--deck-violet) 3% 8%,var(--deck-gold) 8% 11%,var(--deck-orange) 11% 43%,var(--deck-gold) 43% 46%,var(--deck-violet) 46% 56%,var(--deck-gold) 56% 59%,var(--deck-orange) 59% 90%,var(--deck-gold) 90% 93%,var(--deck-violet) 93% 98%,#6b5a4a 98%)" role="img" aria-label="Two decks of flag-themed cards"></div><p class="post-title">At vero eosiusto<br>nissimucimu</p></div>
    <div class="post" style="left:485px"><div class="post-img" style="background:radial-gradient(ellipse at 52% 45%,#3e5eb9 0%,#b3191d 9%,transparent 16%),linear-gradient(160deg,#a9b3bd,#6a7b90 55%,#1f2d45)" role="img" aria-label="Person holding up a flag-themed playing card"></div><p class="post-title">At vero eosiusto<br>nissimucimu</p></div>
    <div class="post" style="left:780px"><div class="post-img" style="background:linear-gradient(150deg,#1e1e1e 22%,var(--flag-blue) 22% 34%,var(--flag-yellow) 34% 38%,var(--red) 38% 76%,var(--flag-yellow) 76% 80%,var(--flag-blue) 80% 88%,#1e1e1e 88%)" role="img" aria-label="Flag-themed card on dark surface"></div><p class="post-title">At vero eosiusto<br>nissimucimu</p></div>
  </section>

  <div class="deco-card" style="left:887px;top:2575px;width:170px;height:245px;transform:rotate(-5deg)" role="img" aria-label="Ace of hearts card decoration"></div>
  <div class="deco-card" style="left:1040px;top:2680px;width:150px;height:215px;transform:rotate(30deg)" role="img" aria-label="Ace of clubs card decoration"></div>
  <div class="deco-card" style="left:55px;top:2890px;width:175px;height:245px;transform:rotate(-6deg)" role="img" aria-label="Ace of hearts card decoration"></div>
  <div class="deco-card" style="left:205px;top:2970px;width:150px;height:210px;transform:rotate(35deg)" role="img" aria-label="Ace of clubs card decoration"></div>

  <h2 class="section-title" style="top:2510px">FAQ’s</h2>
  <div class="faq" style="top:2587px">
    <div class="faq-item"><span class="plus"></span>At vero eos et accusamto odio dignissimos ducimu?</div>
    <div class="faq-item"><span class="plus"></span>At vero eos et accusamto odio dignissimos ducimu?</div>
    <div class="faq-item"><span class="plus"></span>At vero eos et accusamto odio dignissimos ducimu?</div>
    <div class="faq-item"><span class="plus"></span>At vero eos et accusamto odio dignissimos ducimu?</div>
    <div class="faq-item"><span class="plus"></span>At vero eos et accusamto odio dignissimos ducimu?</div>
    <div class="faq-item"><span class="plus"></span>At vero eos et accusamto odio dignissimos ducimu?</div>
  </div>

  <footer class="site-footer" role="contentinfo"></footer>
  <div class="emblem"><div class="emblem-mark" role="img" aria-label="Eswatini flag on a pole"></div></div>

  <div class="contact" style="left:233px">
    <svg width="40" height="40" viewBox="0 0 40 40"><circle cx="20" cy="20" r="18" fill="#fff"/><path d="M14 11c-2 1-3 3-2 6 2 6 7 11 13 13 3 1 5 0 6-2l-4-4-3 2c-3-1-6-4-7-7l2-3z" fill="#2b3f8e"/></svg>
    <span>Corporate Office :<br>+268 7612 3450</span>
  </div>
  <div class="contact" style="left:490px;top:3223px">
    <svg width="40" height="40" viewBox="0 0 40 40"><circle cx="20" cy="20" r="18" fill="#fff"/><path d="M14 11c-2 1-3 3-2 6 2 6 7 11 13 13 3 1 5 0 6-2l-4-4-3 2c-3-1-6-4-7-7l2-3z" fill="#2b3f8e"/></svg>
    <span>International Branch:<br>+1 (555) 014-2290</span>
  </div>
  <div class="contact" style="left:743px;top:3223px">
    <svg width="44" height="32" viewBox="0 0 44 32" fill="none" stroke="#fff" stroke-width="2.5"><rect x="2" y="2" width="40" height="28"/><path d="M2 2l20 16L42 2M2 30l15-14M42 30L27 16"/></svg>
    <span>Email:<br>info@velmoran.example</span>
  </div>
  <div class="footer-rule"></div>
  <div class="socials"><span></span><span></span><span></span><span></span></div>
  <p class="copyright">© 2020 All Rights Are Reserved. Terms of Use | Privacy Policy</p>
  <div class="payments"><span></span><span></span><span></span><span></span></div>

</div>
</body>
</html>
```